Business Card Design

We recently had a new logo designed by Pixel Harbor. Now we want to create new business cards and letterhead that compliment our new logo.

We are audiologists in private practice specializing in hearing evaluations and fitting hearing aids. We want a clean and professional card.

We need business cards for each audiologist. The names and titles are:
Marnie Ostrova, AuD
Audiologist

Jen Tarbel, AuD
Audiologist

Corvina Plesk, AuD
Audiologist

We also need a business card with no provider. Just a generic one.

Finally, we need an appointment card. This is what the front desk uses to give to the patient with their next appointment date and time.

Target Market(s)

Our clients tend to be highly educated. They are older so the cards should be clean and easy to read. No squirrely font please.

Industry/Entity Type

Business

Contact Information for Business Card

20731 8th Ave NE, suite 417
Seattle, WA 98177
206-592-8074

Requirements
Must have
• Clean
Easy to read
Professional
Modern but approachable / warm
Should not have
• Other pictures besides the logo

```html
<!DOCTYPE html>
<html lang="en">
<head>
<meta charset="utf-8">
<title>Brightwater Hearing Services — Business Card</title>
<link rel="stylesheet" href="https://fonts.googleapis.com/css2?family=Open+Sans:wght@400;600;700&display=swap">
<style>
  :root {
    --backdrop: #dfe3e8;
    --card: #f5f5f5;
    --ink: #1f1f1f;
    --ink-soft: #2e2e2e;
    --navy: #2b3660;
    --teal: #3fae96;
  }
  html, body {
    margin: 0;
    width: 1200px;
    height: 1000px;
    overflow: hidden;
    background: var(--backdrop);
    font-family: "Open Sans", Arial, sans-serif;
  }
  .business-card {
    position: absolute;
    left: 100px;
    top: 215px;
    width: 1000px;
    height: 571px;
    background: var(--card);
    overflow: hidden;
    box-shadow: 0 6px 18px rgba(40, 50, 70, 0.18);
  }
  .accent-tab {
    position: absolute;
    right: 0;
    top: 62px;
    width: 18px;
    height: 34px;
    background: var(--teal);
  }
  .brand {
    position: absolute;
    left: 70px;
    top: 372px;
    display: flex;
    align-items: center;
    gap: 18px;
  }
  .brand-dot {
    width: 84px;
    height: 84px;
    border-radius: 50%;
    background: var(--navy);
    flex: none;
  }
  .brand-name {
    margin: 0;
    font-weight: 600;
    color: var(--ink-soft);
    font-size: 32px;
    line-height: 1.1;
    letter-spacing: 0.5px;
    text-transform: uppercase;
  }
  .provider {
    position: absolute;
    left: 560px;
    top: 168px;
    color: var(--ink);
  }
  .provider-name {
    margin: 0;
    font-weight: 700;
    font-size: 31px;
    line-height: 1.2;
  }
  .provider-title {
    margin: 2px 0 0;
    font-size: 24px;
    color: var(--ink-soft);
  }
  .address {
    margin: 36px 0 0;
    font-style: normal;
    font-size: 24px;
    line-height: 1.3;
    color: var(--ink-soft);
  }
  .phone {
    margin: 28px 0 0;
    font-size: 24px;
    color: var(--ink-soft);
  }
</style>
</head>
<body>
  <div class="business-card">
    <div class="accent-tab"></div>

    <div class="brand">
      <div class="brand-dot"></div>
      <p class="brand-name">Brightwater<br>Hearing Services</p>
    </div>

    <div class="provider">
      <p class="provider-name">Marnie Ostrova, AuD</p>
      <p class="provider-title">Audiologist</p>
      <address class="address">20731 8th Ave NE,<br>suite 417 Seattle, WA 98177</address>
      <p class="phone">p : 206-592-8074</p>
    </div>
  </div>
</body>
</html>
```